I need a website, primarily a landing page, for my company, Harlow Ridge. A sales training and cons

I need a web design/landing page for a new sales training and consulting company, harlow ridge. We perform "sales experiments" aimed at each individual or team, where we assist in helping them identify their strengths, through a series of "sales experiments" that we can tailor based on the individual and what they're trying to accomplish.

```html
<!DOCTYPE html>
<html lang="en">
<head>
<meta charset="utf-8">
<title>Harlow Ridge — Sales Training &amp; Consulting</title>
<link href="https://fonts.googleapis.com/css2?family=Lato:wght@400;700;900&display=swap" rel="stylesheet">
<style>
:root{
  --blue:#1a5fb4;
  --blue-deep:#0f4c9c;
  --ink:#1d1d1f;
  --grey:#6b6b6b;
  --light:#d9dde3;
  --dark:#2b2d31;
  --black:#0b0b0c;
  --white:#ffffff;
  --star:#f4b400;
}
*{margin:0;padding:0;box-sizing:border-box}
html,body{width:1200px;height:4557px;overflow:hidden;background:var(--white)}
body{font-family:'Lato',sans-serif;color:var(--ink);position:relative}
.abs{position:absolute}
.center{left:0;width:1200px;text-align:center}
.photo{position:absolute}

/* header */
.topline{top:0;left:0;width:1200px;height:5px;background:var(--blue)}
.header{top:5px;left:0;width:1200px;height:117px;background:var(--white);z-index:3}
.contact-bar{right:120px;top:34px;font-size:14px;color:var(--ink)}
.contact-bar span{margin-left:10px}
.nav{top:76px;left:497px;display:flex;font-size:15px;font-weight:700}
.nav a{color:var(--ink);text-decoration:none;margin-right:38px}
.search{left:1072px;top:78px}
.logo{left:115px;top:-12px;width:204px;height:204px;border-radius:50%;background:var(--white);z-index:4;box-shadow:0 2px 6px rgba(0,0,0,.12);text-align:center}
.logo .mark{display:block;margin:48px auto 0;width:46px;height:46px;border-radius:50%;border:4px solid var(--blue)}
.logo .name{display:block;margin-top:16px;font-size:20px;font-weight:900;color:var(--blue);letter-spacing:1px}

/* hero */
.hero{top:122px;left:0;width:1200px;height:690px;background:linear-gradient(120deg,#4c5761 0%,#6f7881 40%,#a3acb5 70%,#c6ccd1 100%)}
.hero-title{top:300px;font-size:70px;font-weight:900;color:var(--white);letter-spacing:1px}
.hero-sub{top:395px;font-size:19px;color:var(--white)}
.btn{display:inline-block;background:var(--blue);color:var(--white);font-weight:700;border-radius:26px;text-transform:uppercase}
.hero-btn{top:465px;left:503px;width:194px;height:48px;line-height:48px;font-size:16px;text-align:center}
.dots{top:650px;left:551px;display:flex;gap:8px}
.dots i{width:11px;height:11px;border-radius:50%;border:2px solid var(--white);display:block}
.dots i.on{background:var(--white)}

/* section headings */
.h2{font-size:40px;font-weight:900;text-transform:uppercase}
.h2 .b{color:var(--blue)}
.divider{left:500px;width:200px;height:14px}

/* welcome */
.welcome-p{top:985px;left:170px;width:860px;text-align:center;font-size:13px;line-height:31px;color:var(--grey)}
.caption{font-size:23px;font-weight:700;color:var(--blue);text-align:center;width:420px}
.badge{left:553px;top:1361px;width:92px;height:92px;border-radius:50%;background:var(--white);box-shadow:0 0 0 2px var(--light)}

/* services */
.services{top:1555px;left:0;width:1200px;height:840px;background:linear-gradient(160deg,#26282c 0%,#3b3e43 45%,#55585d 100%)}
.svc{width:300px;text-align:center;color:var(--white)}
.svc .ring{width:148px;height:148px;border-radius:50%;border:4px solid var(--white);margin:0 auto;display:flex;align-items:center;justify-content:center}
.svc .ring span{width:118px;height:118px;border-radius:50%;background:var(--white);display:flex;align-items:center;justify-content:center}
.svc h3{font-size:21px;font-weight:700;margin-top:26px}
.svc p{font-size:13px;line-height:24px;margin-top:8px}

/* blog */
.card{width:298px}
.card .img{height:195px}
.card h4{font-size:15px;font-weight:700;margin-top:28px}
.card .meta{font-size:12px;color:var(--grey);margin-top:10px}
.card .meta b{color:var(--blue);font-weight:400}
.card p{font-size:12px;color:var(--grey);line-height:24px;margin-top:10px}
.card .more{font-size:12px;font-weight:900;color:var(--blue);margin-top:8px;display:block}

/* testimonials */
.clients{top:3071px;left:0;width:1200px;height:510px;background:var(--blue-deep)}
.quote{width:320px;color:var(--white)}
.quote .av{width:74px;height:74px;border-radius:50%;border:3px solid var(--white);background:linear-gradient(#b9a79a,#7d6c62);float:left}
.quote .txt{margin-left:92px;font-size:11px;line-height:22px}
.quote .txt b{font-size:24px;vertical-align:-6px;margin-right:4px}
.quote .who{margin-left:92px;margin-top:10px;font-size:10px;font-weight:900;text-transform:uppercase}
.quote .role{margin-left:92px;font-size:9px;font-style:italic}
.quote .stars{clear:both;padding-top:30px;margin-left:92px;color:var(--star);font-size:22px;letter-spacing:3px}
.arrow{width:34px;height:34px;border-radius:50%;border:2px solid rgba(255,255,255,.6);color:var(--white);text-align:center;line-height:30px;font-size:16px}

/* social feed + newsletter */
.fb-title{left:115px;top:3690px;font-size:31px;font-weight:700}
.fb-box{left:115px;top:3752px;width:371px;height:275px;border:1px solid var(--light);background:var(--white)}
.fb-cover{left:8px;top:8px;width:353px;height:158px;background:linear-gradient(120deg,#3d4b5a,#7d8a97)}
.fb-name{left:110px;top:20px;color:var(--white);font-size:15px;font-weight:700}
.fb-likes{left:110px;top:40px;color:var(--white);font-size:12px}
.fb-logo{left:20px;top:14px;width:70px;height:70px;background:var(--white)}
.fb-btn{top:118px;height:26px;line-height:26px;background:#f3f4f6;color:var(--ink);font-size:13px;font-weight:700;padding:0 12px;border:1px solid #cbd0d6}
.fb-note{left:12px;top:178px;font-size:12px;color:var(--grey)}
.fb-face{top:205px;width:48px;height:48px;background:linear-gradient(#8c7a6e,#5a6570)}
.news-h{left:559px;top:3690px;font-size:31px;font-weight:700;line-height:44px;color:var(--ink)}
.news-h .b{color:var(--blue)}
.field{height:44px;border:1px solid #c9ced4;font-size:13px;color:var(--grey);padding:0 20px;line-height:42px}
.sub-btn{left:559px;top:3947px;width:172px;height:44px;line-height:44px;text-align:center;font-size:14px}

/* footer */
.footer{top:4110px;left:0;width:1200px;height:447px;background:var(--black);color:var(--white)}
.fh{font-size:21px;font-weight:700}
.fl{font-size:14px}
.links a{display:block;color:var(--white);text-decoration:none;font-size:13px;margin-bottom:15px}
.soc{display:flex;align-items:center;gap:14px;font-size:13px}
.soc i{width:38px;height:38px;border-radius:50%;border:2px solid var(--white);display:block}
.foot-line{left:155px;top:4487px;width:930px;height:1px;background:#333}
.copy{top:4515px;font-size:12px}
</style>
</head>
<body>

<!-- header -->
<div class="abs topline"></div>
<header class="abs header">
  <div class="abs contact-bar">
    <svg width="12" height="12" viewBox="0 0 24 24"><path d="M6.6 10.8a15 15 0 006.6 6.6l2.2-2.2a1 1 0 011-.25 11.4 11.4 0 003.6.6 1 1 0 011 1V20a1 1 0 01-1 1A17 17 0 013 4a1 1 0 011-1h3.5a1 1 0 011 1c0 1.25.2 2.45.6 3.6a1 1 0 01-.25 1z" fill="#1d1d1f"/></svg>
    <span>Phone : 1 555 014 2288</span>
    <span style="color:#bbb">|</span>
    <svg width="13" height="10" viewBox="0 0 26 20" style="margin-left:10px"><rect width="26" height="20" rx="2" fill="#1a5fb4"/><path d="M1 2l12 9 12-9" stroke="#fff" stroke-width="2" fill="none"/></svg>
    <span style="margin-left:4px">Email : hello@harlowridge.co</span>
  </div>
  <nav class="abs nav">
    <a href="#">Home</a><a href="#">About Us</a><a href="#">Services</a><a href="#">Blog</a><a href="#">Contact Us</a><a href="#">Reviews</a>
  </nav>
  <svg class="abs search" width="16" height="16" viewBox="0 0 24 24"><circle cx="10" cy="10" r="7" stroke="#1a5fb4" stroke-width="3" fill="none"/><path d="M15 15l7 7" stroke="#1a5fb4" stroke-width="3"/></svg>
</header>
<div class="abs logo">
  <i class="mark"></i>
  <span class="name">HARLOW RIDGE</span>
</div>

<!-- hero -->
<section class="abs hero">
  <div class="photo" role="img" aria-label="Business people shaking hands across a meeting table" style="inset:0"></div>
</section>
<h1 class="abs center hero-title">HARLOW RIDGE</h1>
<p class="abs center hero-sub">Sed ut perspiciatis unde omnis iste natus error sit voluptatem accusantium</p>
<a class="abs btn hero-btn">Read more &#10140;</a>
<div class="abs dots"><i></i><i></i><i></i><i></i><i class="on"></i></div>
<svg class="abs" style="top:700px;left:0" width="1200" height="115" viewBox="0 0 1200 115" preserveAspectRatio="none">
  <path d="M0 95 C250 115 520 105 760 70 C950 40 1100 20 1200 30 L1200 115 L0 115Z" fill="#fff"/>
  <path d="M0 88 C250 108 520 98 760 63 C950 33 1100 13 1200 23" stroke="#1a5fb4" stroke-width="7" fill="none"/>
  <path d="M0 80 C250 100 520 90 760 55 C950 25 1100 5 1200 15" stroke="#0b2a55" stroke-width="3" fill="none"/>
</svg>

<!-- welcome -->
<h2 class="abs center h2" style="top:862px"><span class="b">Welcome to</span> Harlow Ridge</h2>
<svg class="abs divider" style="top:941px" viewBox="0 0 200 14"><line x1="0" y1="7" x2="86" y2="7" stroke="#ccc"/><line x1="114" y1="7" x2="200" y2="7" stroke="#ccc"/><circle cx="100" cy="7" r="5" fill="none" stroke="#1a5fb4" stroke-width="2"/></svg>
<p class="abs welcome-p">Sed ut perspiciatis unde omnis iste natus error sit voluptatem accusantium doloremque laudantium, totam rem aperiam, eaque ipsa quae ab illo inventore veritatis et quasi architecto beatae vitae dicta sunt explicabo nemo enim ipsam voluptatem quia voluptas sit</p>
<div class="photo" role="img" aria-label="Trainer presenting to a seated team in a bright office" style="left:158px;top:1085px;width:419px;height:322px;background:linear-gradient(135deg,#d7dde2,#8f9aa3)"></div>
<div class="photo" role="img" aria-label="Two consultants shaking hands over a desk" style="left:623px;top:1085px;width:419px;height:322px;background:linear-gradient(135deg,#c9d2da,#5f6c78)"></div>
<div class="abs badge"></div>
<div class="abs caption" style="left:158px;top:1430px">Sales training</div>
<div class="abs caption" style="left:623px;top:1430px">Consulting</div>

<!-- services -->
<section class="abs services">
  <div class="photo" role="img" aria-label="Hands reviewing charts and documents on a desk" style="inset:0;background:linear-gradient(160deg,rgba(0,0,0,.1),rgba(255,255,255,.06))"></div>
</section>
<svg class="abs" style="top:1540px;left:0" width="1200" height="120" viewBox="0 0 1200 120" preserveAspectRatio="none">
  <path d="M0 0 L1200 0 L1200 20 C950 25 700 100 420 100 C250 100 100 85 0 80Z" fill="#fff"/>
</svg>
<h2 class="abs center h2" style="top:1757px;color:#fff">Our Services</h2>
<svg class="abs divider" style="top:1831px" viewBox="0 0 200 14"><line x1="0" y1="7" x2="86" y2="7" stroke="#aaa"/><line x1="114" y1="7" x2="200" y2="7" stroke="#aaa"/><circle cx="100" cy="7" r="5" fill="none" stroke="#fff" stroke-width="2"/></svg>
<div class="abs svc" style="left:93px;top:1915px">
  <div class="ring"><span><svg width="60" height="60" viewBox="0 0 60 60" fill="none" stroke="#1a5fb4" stroke-width="2.5"><rect x="12" y="10" width="36" height="26"/><path d="M17 30l8-8 6 5 10-10"/><path d="M30 36v14M22 50h16"/></svg></span></div>
  <h3>Sed utperspic</h3>
  <p>Lorem ipsum dolor sit amet consectetur<br>adipiscing sed doeiusmodnim</p>
</div>
<div class="abs svc" style="left:448px;top:1915px">
  <div class="ring"><span><svg width="60" height="60" viewBox="0 0 60 60" fill="none" stroke="#1a5fb4" stroke-width="2.5"><circle cx="30" cy="30" r="20"/><ellipse cx="30" cy="30" rx="9" ry="20"/><path d="M10 30h40M14 20h32M14 40h32"/></svg></span></div>
  <h3>Nulla pariatur</h3>
  <p>Lorem ipsum dolor sit amet consectetur<br>adipiscing sed doeiusmodnim</p>
</div>
<div class="abs svc" style="left:807px;top:1915px">
  <div class="ring"><span><svg width="60" height="60" viewBox="0 0 60 60" fill="none" stroke="#1a5fb4" stroke-width="2.5"><rect x="18" y="12" width="24" height="16" rx="2"/><circle cx="14" cy="38" r="5"/><circle cx="46" cy="38" r="5"/><path d="M6 52c2-6 14-6 16 0M38 52c2-6 14-6 16 0M30 28v10M14 33v-3h32v3"/></svg></span></div>
  <h3>Dolorque laudan</h3>
  <p>Lorem ipsum dolor sit amet consectetur<br>adipiscing sed doeiusmodnim</p>
</div>
<svg class="abs" style="top:2240px;left:0" width="1200" height="160" viewBox="0 0 1200 160" preserveAspectRatio="none">
  <path d="M0 130 C300 150 650 130 900 80 C1050 50 1150 15 1200 5 L1200 160 L0 160Z" fill="#fff"/>
  <path d="M0 122 C300 142 650 122 900 72 C1050 42 1150 7 1200 -3" stroke="#1a5fb4" stroke-width="8" fill="none"/>
</svg>

<!-- blog -->
<h2 class="abs center h2" style="top:2456px"><span class="b">Blog</span> Posts</h2>
<svg class="abs divider" style="top:2533px" viewBox="0 0 200 14"><circle cx="100" cy="7" r="5" fill="none" stroke="#1a5fb4" stroke-width="2"/></svg>
<article class="abs card" style="left:112px;top:2597px">
  <div class="img" role="img" aria-label="Laptop and tablet on an office desk" style="background:linear-gradient(135deg,#e4e8ec,#7e8a96)"></div>
  <h4>Sed quia consequuntur maolores..</h4>
  <div class="meta"><b>&#9679;</b> 255 views &nbsp; <b>&#9829;</b> 29</div>
  <p>But I must explain to you how all this mistaken<br>idea of denouncing pleasure</p>
  <span class="more">READ MORE</span>
</article>
<article class="abs card" style="left:450px;top:2597px">
  <div class="img" role="img" aria-label="Team collaborating around a meeting table" style="background:linear-gradient(135deg,#dfe5ea,#6f7d8a)"></div>
  <h4>Sed quia consequuntur maolores..</h4>
  <div class="meta"><b>&#9679;</b> 255 views &nbsp; <b>&#9829;</b> 29</div>
  <p>But I must explain to you how all this mistaken<br>idea of denouncing pleasure</p>
  <span class="more">READ MORE</span>
</article>
<article class="abs card" style="left:787px;top:2597px">
  <div class="img" role="img" aria-label="Colleagues talking at a desk with a laptop" style="background:linear-gradient(135deg,#e8e1d8,#9a8676)"></div>
  <h4>Sed quia consequuntur maolores..</h4>
  <div class="meta"><b>&#9679;</b> 255 views &nbsp; <b>&#9829;</b> 29</div>
  <p>But I must explain to you how all this mistaken<br>idea of denouncing pleasure</p>
  <span class="more">READ MORE</span>
</article>

<!-- testimonials -->
<section class="abs clients"></section>
<h2 class="abs center h2" style="top:3167px;color:#fff;font-size:38px">What Clients Say</h2>
<svg class="abs divider" style="top:3241px" viewBox="0 0 200 14"><line x1="0" y1="7" x2="86" y2="7" stroke="#8fb0de"/><line x1="114" y1="7" x2="200" y2="7" stroke="#8fb0de"/><circle cx="100" cy="7" r="5" fill="none" stroke="#fff" stroke-width="2"/></svg>
<div class="abs arrow" style="left:30px;top:3361px">&#8249;</div>
<div class="abs arrow" style="left:1135px;top:3361px">&#8250;</div>
<div class="abs quote" style="left:97px;top:3305px">
  <div class="av" role="img" aria-label="Client portrait"></div>
  <div class="txt"><b>&ldquo;</b>At vero eos et accusamus et iusto odio dignissimos ducimus qui blanditiis praesent lum voluptatum deleniti atq.</div>
  <div class="who">Marla Quenby</div><div class="role">Financial Services Professional</div>
  <div class="stars">&#9733;&#9733;&#9733;&#9733;&#9734;</div>
</div>
<div class="abs quote" style="left:449px;top:3305px">
  <div class="av" role="img" aria-label="Client portrait" style="background:linear-gradient(#9aa0a6,#4f565d)"></div>
  <div class="txt"><b>&ldquo;</b>At vero eos et accusamus et iusto odio digni ssimos ducimus qui blanditiis praesent lum volup tatum deleniti atq.</div>
  <div class="who">Tobias R. Fenwick</div><div class="role">National Sales Fellow at the Institute</div>
  <div class="stars">&#9733;&#9733;&#9733;&#9733;&#9733;</div>
</div>
<div class="abs quote" style="left:789px;top:3305px">
  <div class="av" role="img" aria-label="Client portrait" style="background:linear-gradient(#c7b2a0,#8a715f)"></div>
  <div class="txt"><b>&ldquo;</b>At vero eos et accusamus et iusto odio dignissimos ducimus qui blanditiis praesent lum voluptatum deleniti atq.</div>
  <div class="who">Lena Ostrow</div><div class="role">Creative Strategist | Entrepreneur &amp; Upcoming</div>
  <div class="stars">&#9733;&#9733;&#9733;&#9733;&#9734;</div>
</div>

<!-- social feed + newsletter -->
<h3 class="abs fb-title">Friendbook</h3>
<div class="abs fb-box">
  <div class="abs fb-cover" role="img" aria-label="Page cover image">
    <div class="abs fb-logo"></div>
    <div class="abs fb-name">HARLOW RIDGE</div>
    <div class="abs fb-likes">4,893 likes</div>
    <div class="abs fb-btn" style="left:12px">Like Page</div>
    <div class="abs fb-btn" style="left:245px">&#9998; Sign Up</div>
  </div>
  <div class="abs fb-note">Be the first of your friends to like this</div>
  <div class="abs fb-face" role="img" aria-label="Follower thumbnail" style="left:12px"></div>
  <div class="abs fb-face" role="img" aria-label="Follower thumbnail" style="left:68px"></div>
  <div class="abs fb-face" role="img" aria-label="Follower thumbnail" style="left:124px"></div>
  <div class="abs fb-face" role="img" aria-label="Follower thumbnail" style="left:180px"></div>
  <div class="abs fb-face" role="img" aria-label="Follower thumbnail" style="left:236px"></div>
  <div class="abs fb-face" role="img" aria-label="Follower thumbnail" style="left:292px"></div>
</div>
<h3 class="abs news-h"><span class="b">Sign up for our Newsletter to stay</span><br>up to date on the latest &nbsp;deals!</h3>
<div class="abs field" style="left:559px;top:3805px;width:270px">First Name</div>
<div class="abs field" style="left:845px;top:3805px;width:270px">Last Name</div>
<div class="abs field" style="left:559px;top:3870px;width:556px">Email</div>
<a class="abs btn sub-btn">Subscribe Now!</a>

<!-- footer -->
<svg class="abs" style="top:4040px;left:0" width="1200" height="110" viewBox="0 0 1200 110" preserveAspectRatio="none">
  <path d="M0 110 L0 50 C200 30 420 40 700 75 C900 95 1080 70 1200 55 L1200 110Z" fill="#0b0b0c"/>
  <path d="M0 42 C200 22 420 32 700 67 C900 87 1080 62 1200 47" stroke="#1a5fb4" stroke-width="7" fill="none"/>
</svg>
<footer class="abs footer">
  <div class="abs fh" style="left:155px;top:170px">Contact Us</div>
  <div class="abs fl" style="left:155px;top:222px">&#9742;&nbsp; Phone : 1 555 014 2288</div>
  <div class="abs fl" style="left:155px;top:262px">&#9993;&nbsp; Email : hello@harlowridge.co</div>
  <div class="abs fh" style="left:520px;top:170px">Quick Links</div>
  <div class="abs links" style="left:520px;top:222px"><a>Home</a><a>About Us</a><a>Services</a><a>Blog</a></div>
  <div class="abs links" style="left:623px;top:222px"><a>Reviews</a><a>Contact Us</a></div>
  <div class="abs fh" style="left:805px;top:170px">Stay Connected</div>
  <div class="abs soc" style="left:805px;top:216px"><i></i>Friendbook</div>
  <div class="abs soc" style="left:948px;top:216px"><i></i>Chirper</div>
  <div class="abs soc" style="left:805px;top:275px"><i></i>Snapgram</div>
</footer>
<div class="abs foot-line"></div>
<div class="abs center copy" style="color:#fff">2018 &copy; Harlow Ridge. All rights reserved. &nbsp;|&nbsp; Privacy policy</div>

</body>
</html>
```